Dog treat Package Design

We’re looking for a creative and professional designer to develop eye-catching packaging for our upcoming line of premium dog treats under the Tail Nibbles brand.
The design should reflect quality, trust, and natural nutrition, appealing to dog owners who value healthy, high-end pet products.
What We Need
Full packaging design for a resealable stand-up pouch (approx. 130 × 210 + 60 mm)
Front and back layout including space for logo, product name, ingredients, nutrition panel, barcode, and storage instructions
Print-ready files (with dielines, bleeds, and crop marks)
Editable source file (AI / PSD preferred)
3D mock-up or realistic rendering for presentation
Design Direction
Clean, minimal, and modern look with a premium feel
Use natural tones (e.g. earthy browns, creams, muted greens, or soft neutrals)
Should convey trust, wellness, and craftsmanship
Incorporate subtle texture or illustration that hints at natural ingredients or happy, healthy dogs
Must be consistent across potential product variations (e.g. chicken, beef, lamb treats)
Target Audience
Pet owners who value nutrition, quality ingredients, and design aesthetics — typically aged 25–50, with a focus on healthy, Australian-made pet products.
Deliverables
2 initial design concepts
Up to 2 revision rounds
Final deliverables in:
Print-ready PDF (CMYK)
Editable AI/PSD
High-resolution mock-ups
Design style similar to Maple Paws
Updates
Target Market(s)
People with pets - Premium
Look and feel
Each slider illustrates characteristics of the customer's brand and the style your logo design should communicate.

```html
<!DOCTYPE html>
<html lang="en">
<head>
<meta charset="utf-8">
<title>Tail Nibbles – Duck Jerky Pouch</title>
<link rel="stylesheet" href="https://fonts.googleapis.com/css2?family=Abril+Fatface&family=Montserrat:wght@400;500;600&display=swap">
<style>
  :root {
    --page: #f3f3f5;
    --lime: #c9dd3e;
    --lime-soft: #d6e45a;
    --green-mid: #a5cc3c;
    --green-deep: #6fa634;
    --gray-light: #948a93;
    --gray-mid: #6b6169;
    --gray-dark: #3f383d;
    --cream: #f6f1dc;
    --white: #ffffff;
    --ink: #5a5a5a;
    --gold: #a97a2c;
    --jerky: #8a4a2a;
  }
  * { margin: 0; padding: 0; box-sizing: border-box; }
  html, body { width: 1200px; height: 2864px; overflow: hidden; background: var(--page); }
  .canvas { position: relative; width: 1200px; height: 2864px; }
  .pouch-front {
    position: absolute; left: 183px; top: 172px; width: 828px; height: 1417px;
    background: var(--lime); overflow: hidden; font-family: "Montserrat", sans-serif;
  }
  .pouch-art { position: absolute; inset: 0; }
  .brand-mark {
    position: absolute; left: 120px; top: 346px; width: 234px; height: 234px;
    border-radius: 50%; background: var(--white);
    display: flex; align-items: center; justify-content: center;
  }
  .brand-name { font-size: 20px; font-weight: 500; letter-spacing: 2px; color: var(--ink); text-transform: uppercase; }
  .product-title {
    position: absolute; left: 372px; top: 392px; width: 400px;
    font-family: "Abril Fatface", serif; font-size: 96px; line-height: 116px; font-weight: 400;
    color: var(--cream); text-align: center; letter-spacing: 1px;
  }
  .quality-seal {
    position: absolute; left: 478px; top: 673px; width: 188px; height: 188px;
    border-radius: 50%; background: var(--white); border: 5px solid var(--gold);
    display: flex; flex-direction: column; align-items: center; justify-content: center; gap: 8px;
  }
  .seal-label { font-size: 14px; font-weight: 600; letter-spacing: 1px; color: var(--gray-dark); }
  .seal-emblem { width: 80px; height: 80px; border-radius: 50%; background: var(--gold); }
  .feature-row {
    position: absolute; left: 118px; top: 1160px; width: 597px;
    display: flex; justify-content: space-between; list-style: none;
  }
  .feature {
    width: 68px; height: 68px; border-radius: 50%; background: var(--white);
    border: 2px solid var(--gray-mid);
    display: flex; flex-direction: column; align-items: center; justify-content: center;
  }
  .feature-label { font-size: 6.5px; font-weight: 600; color: var(--gray-dark); text-align: center; line-height: 1.1; margin-bottom: 3px; }
  .feature svg { width: 24px; height: 24px; }
  .pack-info {
    position: absolute; top: 1246px; font-size: 24px; font-weight: 500; color: var(--white); letter-spacing: .5px;
  }
  .life-stages { left: 125px; }
  .net-weight { left: 550px; }
</style>
</head>
<body>
<main class="canvas">
  <section class="pouch-front">
    <svg class="pouch-art" width="828" height="1417" viewBox="0 0 828 1417">
      <rect role="img" aria-label="Faint leafy branch decoration" x="367" y="0" width="461" height="472" fill="var(--lime-soft)" opacity=".7"/>
      <rect class="top-band" x="100" y="0" width="267" height="470" fill="var(--white)" opacity=".9"/>
      <path class="wave-outer" fill="var(--green-deep)" d="M0 405 C90 380 170 420 250 470 C340 520 440 520 540 570 C640 610 740 600 828 630 L828 1110 C740 1090 680 1160 580 1140 C480 1120 420 1200 300 1180 C200 1160 110 1220 0 1200 Z"/>
      <path class="wave-mid" fill="var(--green-mid)" d="M0 470 C90 450 170 480 250 520 C340 570 440 560 540 610 C640 650 740 650 828 680 L828 1160 C730 1140 660 1220 560 1200 C460 1180 400 1260 290 1240 C190 1220 110 1290 0 1270 Z"/>
      <path class="wave-bottom" fill="var(--green-deep)" d="M0 1290 C100 1270 180 1300 280 1330 C380 1360 470 1320 560 1340 C650 1360 740 1320 828 1300 L828 1340 C740 1360 650 1400 560 1380 C470 1360 380 1400 280 1370 C180 1340 100 1320 0 1330 Z"/>
      <path class="wave-gray" fill="var(--gray-light)" d="M40 700 C90 640 200 640 280 610 C360 580 460 600 560 640 C660 680 740 740 790 800 C830 860 770 940 780 1020 C790 1100 720 1140 640 1140 C540 1140 460 1110 380 1140 C290 1170 200 1120 150 1060 C90 990 100 920 70 850 C40 790 10 740 40 700 Z"/>
      <path class="wave-gray-mid" fill="var(--gray-mid)" d="M80 720 C130 675 220 675 290 650 C365 625 455 640 545 675 C635 710 700 760 740 815 C770 865 725 935 732 1005 C740 1075 680 1100 615 1100 C530 1100 460 1075 385 1100 C300 1128 225 1090 180 1040 C130 985 140 925 115 860 C90 805 55 755 80 720 Z"/>
      <path class="wave-gray-deep" fill="var(--gray-dark)" d="M120 745 C170 710 240 710 305 688 C375 665 455 678 535 710 C615 742 665 790 690 840 C712 885 680 945 685 1005 C690 1055 640 1070 590 1068 C520 1066 460 1045 395 1068 C320 1094 255 1062 215 1020 C170 972 180 920 160 865 C140 815 100 770 120 745 Z"/>
      <path role="img" aria-label="Window showing pieces of duck jerky" fill="var(--jerky)" d="M160 770 C205 745 260 745 320 725 C385 705 455 715 525 745 C595 775 635 815 652 860 C668 905 640 955 644 1005 C648 1040 610 1048 570 1046 C505 1043 450 1025 395 1044 C330 1066 275 1040 240 1005 C200 965 210 920 192 875 C175 830 140 790 160 770 Z"/>
    </svg>

    <div class="brand-mark">
      <span class="brand-name">Tail Nibbles</span>
    </div>

    <h1 class="product-title">DUCK<br>JERKY</h1>

    <div class="quality-seal">
      <span class="seal-label">HIGH-QUALITY</span>
      <span class="seal-emblem" role="img" aria-label="Duck illustration"></span>
      <span class="seal-label">DUCK</span>
    </div>

    <ul class="feature-row">
      <li class="feature"><span class="feature-label">100%<br>NATURAL</span>
        <svg viewBox="0 0 26 26"><path d="M13 22 V12 M13 14 C8 14 5 10 5 6 C10 6 13 9 13 14 M13 16 C18 16 21 12 21 8 C16 8 13 11 13 16" fill="none" stroke="var(--gray-dark)" stroke-width="1.6"/></svg></li>
      <li class="feature"><span class="feature-label">FREEZE<br>DRIED</span>
        <svg viewBox="0 0 26 26"><path d="M13 3 V23 M4 8 L22 18 M4 18 L22 8" stroke="var(--gray-dark)" stroke-width="1.8"/></svg></li>
      <li class="feature"><span class="feature-label">100%<br>MONO</span>
        <svg viewBox="0 0 26 26"><path d="M6 20 C10 16 8 10 12 6 M12 20 C16 16 14 10 18 6 M18 20 C22 16 20 10 22 8" fill="none" stroke="var(--gray-dark)" stroke-width="1.6"/></svg></li>
      <li class="feature"><span class="feature-label">WITHOUT<br>ADDITIVES</span>
        <svg viewBox="0 0 26 26"><path d="M10 4 H16 M11 4 V11 L5 21 H21 L15 11 V4 M5 23 L21 5" fill="none" stroke="var(--gray-dark)" stroke-width="1.6"/></svg></li>
      <li class="feature"><span class="feature-label">HIGH IN<br>PROTEIN</span>
        <svg viewBox="0 0 26 26"><path d="M13 4 L22 13 H17 V22 H9 V13 H4 Z" fill="none" stroke="var(--gray-dark)" stroke-width="1.8"/></svg></li>
      <li class="feature"><span class="feature-label">HIGH IN<br>FLAVOR</span>
        <svg viewBox="0 0 26 26"><circle cx="13" cy="13" r="10" fill="none" stroke="var(--gray-dark)" stroke-width="1.6"/><path d="M8 15 C10 19 16 19 18 15" fill="none" stroke="var(--gray-dark)" stroke-width="1.6"/></svg></li>
    </ul>

    <p class="pack-info life-stages">FOR ALL LIFE STAGES</p>
    <p class="pack-info net-weight">NET'WT. 120g</p>
  </section>
</main>
</body>
</html>
```